Re-design a highly converting profile page for my website

My website allows people to book a mentor for long-term mentorship as well as sessions. I would like to re-design this site within our branding guidelines to give people the best profile possible.

Please give this website a modern look and concentrate on the CTA and conversion rates. This is a highly converting site and it should stay that way or even get better!

Please also keep menu bar & footer in tact

Target Market(s)

Developers, Designers, Entrepreneurs in the Tech industry

Number of Pages Required

1 page

Requirements
Must have
• Strong CTA, existing color palette, testimonials and major elements
Nice to have
• Modern look, easy to see CTA, easy to scan offer. Not too crowded
Should not have
• No reporpusing. It is and stays a profile page

```html
<!DOCTYPE html>
<html lang="en">
<head>
<meta charset="utf-8">
<title>Mentor Profile</title>
<link href="https://fonts.googleapis.com/css2?family=Roboto:wght@300;400;500;700&display=swap" rel="stylesheet">
<style>
:root{
  --nav:#2f3d5c;
  --teal:#00d1b2;
  --teal-soft:#d6f8f0;
  --teal-text:#3f8f7c;
  --bg:#f6f6f6;
  --card:#ffffff;
  --ink:#161616;
  --muted:#333;
  --tag:#f1f1f1;
  --star:#f5b400;
  --dot:#bdbdbd;
}
*{box-sizing:border-box;margin:0;padding:0}
html,body{width:672px;height:1200px;overflow:hidden}
body{background:var(--bg);font-family:'Roboto',sans-serif;color:var(--ink);position:relative}
.abs{position:absolute}
.nav{left:0;top:0;width:672px;height:26px;background:var(--nav)}
.brand{left:59px;top:4px;display:flex;align-items:center;gap:4px;color:#fff;font-size:7px;font-weight:500}
.brand-dot{width:17px;height:17px;border-radius:50%;background:var(--teal)}
.nav-links{right:66px;top:5px;display:flex;align-items:center;gap:10px;font-size:6.6px;color:#fff}
.nav-links span.dim{color:#c9d1e0}
.logout{border:1px solid #fff;border-radius:1px;width:52px;height:15px;display:flex;align-items:center;justify-content:center}
.profile{left:63px;top:44px;width:405px;height:368px;background:var(--card)}
.photo{left:80px;top:60px;width:79px;height:84px;background:linear-gradient(160deg,#f2b3b8,#e9a0a8 60%,#d7a431)}
.stars{left:92px;top:151px;display:flex;gap:3px}
.reviews{left:80px;top:166px;width:79px;text-align:center;font-size:5.5px}
.socials{left:80px;top:186px;width:79px;display:flex;justify-content:center;gap:7px;font-size:6.5px;font-weight:500;color:#1a78c2}
.name{left:173px;top:64px;font-size:17px;font-weight:700}
.loc{left:173px;top:87px;font-size:8.5px;color:var(--teal-text);display:flex;align-items:center;gap:4px}
.role{left:173px;top:111px;font-size:9.5px;font-weight:500}
.tags{left:174px;top:132px;width:270px;display:flex;flex-wrap:wrap;gap:4px 4px}
.tag{background:var(--tag);font-size:5.6px;height:14px;padding:0 8px;display:flex;align-items:center;justify-content:center;min-width:46px}
.tag.on{background:var(--teal-soft);color:var(--teal-text)}
.spots{left:383px;top:44px;width:85px;height:27px;background:var(--teal-soft);color:var(--teal-text);font-size:7.6px;font-weight:500;display:flex;align-items:center;justify-content:center}
.rule{left:173px;top:176px;width:17px;height:2px;background:var(--teal)}
.bio{left:173px;top:184px;width:270px;font-size:6.7px;line-height:12.3px;font-weight:300;color:var(--muted)}
.bio p+p{margin-top:6px}
.info-head{height:19px;background:var(--teal-soft);font-size:7.6px;display:flex;align-items:center;gap:5px;padding-left:6px;width:124px}
.list{font-size:6.9px;font-weight:300;line-height:13.8px;color:var(--muted)}
.more{font-size:6.9px;color:var(--teal-text);font-weight:500}
.trial{left:481px;top:44px;width:78px;height:14px;background:var(--teal-soft);color:var(--teal-text);font-size:6.5px;display:flex;align-items:center;gap:5px;padding-left:5px}
.price{left:484px;top:66px;font-size:25px;font-weight:700;line-height:1}
.per{left:483px;top:93px;font-size:12.5px;font-weight:500}
.btn-apply{left:484px;top:125px;width:125px;height:27px;background:var(--teal);color:#fff;font-size:9px;font-weight:700;display:flex;align-items:center;justify-content:center}
.btn-call{left:484px;top:159px;width:125px;height:27px;border:1px solid var(--ink);font-size:9px;font-weight:500;display:flex;align-items:center;justify-content:center}
h2{font-size:18px;font-weight:700}
.session{top:469px;width:172px;height:130px;background:var(--card)}
.s-tag{left:11px;top:8px;background:var(--teal-soft);color:var(--teal-text);font-size:7px;height:14px;padding:0 6px;display:flex;align-items:center}
.s-price{right:8px;top:6px;font-size:13px;color:var(--teal-text);font-weight:500}
.s-title{left:11px;top:32px;width:155px;font-size:10px;font-weight:500;line-height:14.5px}
.s-time{left:11px;top:69px;font-size:8px;font-weight:500;display:flex;align-items:center;gap:4px}
.s-btn{left:11px;top:97px;width:69px;height:24px;background:var(--teal);color:#fff;font-size:8px;font-weight:500;display:flex;align-items:center;justify-content:center}
.browse{left:274px;top:624px;width:125px;height:27px;background:var(--teal-soft);font-size:8.6px;font-weight:500;display:flex;align-items:center;justify-content:center}
.quote{top:694px;width:325px;height:179px;background:var(--card);border-top:6px solid var(--teal);text-align:center}
.q-text{margin-top:45px;font-size:13.3px;line-height:17px;font-weight:400}
.q-name{margin-top:18px;font-size:11px}
.q-role{margin-top:2px;font-size:7px}
.dots{left:315px;top:897px;display:flex;gap:9px}
.dots i{width:8px;height:8px;border-radius:50%;background:var(--dot)}
.dots i.on{background:var(--ink)}
.mentor{top:972px;width:172px;height:103px;background:var(--card)}
.m-photo{left:8px;top:8px;width:41px;height:41px}
.m-name{left:58px;top:12px;font-size:10px;font-weight:500}
.m-tag{left:58px;top:28px;background:var(--teal-soft);color:var(--teal-text);font-size:7px;height:14px;padding:0 6px;display:flex;align-items:center}
.m-desc{left:8px;top:56px;width:160px;font-size:6.8px;line-height:9.5px}
.m-price{left:8px;top:80px;font-size:9px;font-weight:700;color:var(--teal-text)}
</style>
</head>
<body>

<header class="abs nav">
  <div class="abs brand"><span class="brand-dot"></span>Mentora</div>
  <nav class="abs nav-links">
    <span>Dashboard</span><span class="dim">Management</span><span class="dim">Your Profile</span>
    <svg width="7" height="7" viewBox="0 0 10 10"><path d="M5 0.5 6.3 3.6 9.6 3.8 7 6 7.9 9.3 5 7.5 2.1 9.3 3 6 0.4 3.8 3.7 3.6Z" fill="#c9d1e0"/></svg>
    <span class="logout">Logout</span>
  </nav>
</header>

<section class="abs profile"></section>
<div class="abs photo" role="img" aria-label="Portrait photo of the mentor"></div>
<div class="abs stars">
  <svg width="9" height="9" viewBox="0 0 10 10"><path d="M5 0.5 6.3 3.6 9.6 3.8 7 6 7.9 9.3 5 7.5 2.1 9.3 3 6 0.4 3.8 3.7 3.6Z" fill="#f5b400"/></svg>
  <svg width="9" height="9" viewBox="0 0 10 10"><path d="M5 0.5 6.3 3.6 9.6 3.8 7 6 7.9 9.3 5 7.5 2.1 9.3 3 6 0.4 3.8 3.7 3.6Z" fill="#f5b400"/></svg>
  <svg width="9" height="9" viewBox="0 0 10 10"><path d="M5 0.5 6.3 3.6 9.6 3.8 7 6 7.9 9.3 5 7.5 2.1 9.3 3 6 0.4 3.8 3.7 3.6Z" fill="#f5b400"/></svg>
  <svg width="9" height="9" viewBox="0 0 10 10"><path d="M5 0.5 6.3 3.6 9.6 3.8 7 6 7.9 9.3 5 7.5 2.1 9.3 3 6 0.4 3.8 3.7 3.6Z" fill="#f5b400"/></svg>
  <svg width="9" height="9" viewBox="0 0 10 10"><path d="M5 0.5 6.3 3.6 9.6 3.8 7 6 7.9 9.3 5 7.5 2.1 9.3 3 6 0.4 3.8 3.7 3.6Z" fill="#f5b400"/></svg>
</div>
<div class="abs reviews">(20 REVIEWS)</div>
<div class="abs socials"><span>Facet</span><span>Chirp</span><span>Linkr</span></div>

<h1 class="abs name">Samantha Jones</h1>
<div class="abs loc">
  <svg width="6" height="8" viewBox="0 0 6 8"><path d="M3 0C1.3 0 0 1.3 0 3c0 2.2 3 5 3 5s3-2.8 3-5C6 1.3 4.7 0 3 0Zm0 4.2A1.2 1.2 0 1 1 3 1.8a1.2 1.2 0 0 1 0 2.4Z" fill="#3f8f7c"/></svg>
  Australia
</div>
<div class="abs role">Lead Developer - chirpnet.com &amp; Home</div>
<div class="abs tags">
  <span class="tag on" style="min-width:39px">Design</span>
  <span class="tag">UI/UX</span>
  <span class="tag">React</span>
  <span class="tag" style="min-width:73px">Engineering &amp; Data</span>
  <span class="tag" style="min-width:58px">Landing page</span>
  <span class="tag" style="min-width:51px">Wireframing</span>
  <span class="tag" style="min-width:54px">Mobile Games</span>
</div>
<div class="abs spots">2 Spots Available</div>
<div class="abs rule"></div>
<div class="abs bio">
  <p>Hey, I am Samantha. Sed ut perspiciatis unde omnis iste natus error sit voluptatem accusantium doloremque laudantium, totam rem aperiam, eaque ipsa quae ab illo inventore veritatis et quasi architecto beatae vitae dicta sunt explicabo. Nemo enim ipsam voluptatem quia voluptas sit aspernatur aut odit aut fugit, sed quia shed met consequuntur magni dolores eos qui ratione voluptatem sequi nesciunt.</p>
  <p>Neque porro quisquam est, qui dolorem ipsum quia dolor sit amet, consectetur, adipisci velit, sed quia non numquam eius modi tempora incidunt ut labore et dolore magnam</p>
</div>
<div class="abs info-head" style="left:173px;top:303px">
  <svg width="8" height="8" viewBox="0 0 10 10"><circle cx="5" cy="5" r="4.2" fill="none" stroke="#00d1b2" stroke-width="1.1"/><path d="M5 2.6v3M5 7v.6" stroke="#00d1b2" stroke-width="1.1"/></svg>
  What to expect?
</div>
<div class="abs list" style="left:173px;top:328px">
  <div>-&nbsp;&nbsp;Sed ut perspiciatis unde omnis iste</div>
  <div>-&nbsp;&nbsp;Error sit voluptatem accusantium</div>
  <div>-&nbsp;&nbsp;Doloremque laudantium totam rem</div>
</div>
<div class="abs more" style="left:179px;top:375px">Show More</div>
<div class="abs info-head" style="left:320px;top:303px">
  <svg width="6" height="9" viewBox="0 0 6 9"><path d="M3.6 0 0 5h2.4L1.8 9 6 3.6H3.4Z" fill="#00d1b2"/></svg>
  Average Response Time
</div>
<div class="abs list" style="left:320px;top:328px">Sed ut perspiciatis unde omnis iste</div>

<div class="abs trial">
  <svg width="8" height="7" viewBox="0 0 8 7"><path d="M0 7V3.5L4 0l4 3.5V7Z" fill="#3f8f7c"/></svg>
  7 days free trial
</div>
<div class="abs price">$199</div>
<div class="abs per">per month</div>
<a class="abs btn-apply">Apply for Mentorship</a>
<a class="abs btn-call">Book a Call</a>

<h2 class="abs" style="left:63px;top:436px">Other sessions by Samantha</h2>

<article class="abs session" style="left:63px">
  <span class="abs s-tag">Coaching Session</span><span class="abs s-price">$150</span>
  <h3 class="abs s-title">How to become a Web Product designer</h3>
  <div class="abs s-time"><svg width="9" height="9" viewBox="0 0 10 10"><circle cx="5" cy="5" r="5" fill="#00d1b2"/><path d="M5 2v3l2 1.5" stroke="#fff" stroke-width="1.1" fill="none"/></svg>60 minutes</div>
  <a class="abs s-btn">Book Session</a>
</article>
<article class="abs session" style="left:250px">
  <span class="abs s-tag">Coaching Session</span><span class="abs s-price">$200</span>
  <h3 class="abs s-title">How to become a Data Engineer Product at Northsoft</h3>
  <div class="abs s-time"><svg width="9" height="9" viewBox="0 0 10 10"><circle cx="5" cy="5" r="5" fill="#00d1b2"/><path d="M5 2v3l2 1.5" stroke="#fff" stroke-width="1.1" fill="none"/></svg>60 minutes</div>
  <a class="abs s-btn">Book Session</a>
</article>
<article class="abs session" style="left:437px">
  <span class="abs s-tag">Coaching Session</span><span class="abs s-price">$200</span>
  <h3 class="abs s-title">How to become a Data Engineer Product at Northsoft</h3>
  <div class="abs s-time"><svg width="9" height="9" viewBox="0 0 10 10"><circle cx="5" cy="5" r="5" fill="#00d1b2"/><path d="M5 2v3l2 1.5" stroke="#fff" stroke-width="1.1" fill="none"/></svg>60 minutes</div>
  <a class="abs s-btn">Book Session</a>
</article>
<a class="abs browse">Browse all sessions</a>

<blockquote class="abs quote" style="left:-166px">
  <p class="q-text">Our project was completed<br>on time. We are really happy<br>how everything changed.</p>
  <p class="q-name">Julia Aspen</p><p class="q-role">Creative Manager Stigma Inc</p>
</blockquote>
<blockquote class="abs quote" style="left:174px">
  <p class="q-text">Our project was completed<br>on time. We are really happy<br>how everything changed.</p>
  <p class="q-name">Julia Aspen</p><p class="q-role">Creative Manager Stigma Inc</p>
</blockquote>
<blockquote class="abs quote" style="left:514px">
  <p class="q-text">Our project was completed<br>on time. We are really happy<br>how everything changed.</p>
  <p class="q-name">Julia Aspen</p><p class="q-role">Creative Manager Stigma Inc</p>
</blockquote>
<div class="abs dots"><i class="on"></i><i></i><i></i></div>

<h2 class="abs" style="left:63px;top:938px">Similar Mentors</h2>

<article class="abs mentor" style="left:63px">
  <div class="abs m-photo" role="img" aria-label="Photo of Steve Jason" style="background:linear-gradient(135deg,#f07a1a,#5a4a44)"></div>
  <h3 class="abs m-name">Steve Jason</h3><span class="abs m-tag">Lead Developer</span>
  <p class="abs m-desc">We believe Steve can be a good fit as well for mentorship you are looking for!</p>
  <p class="abs m-price">$250/Month</p>
</article>
<article class="abs mentor" style="left:250px">
  <div class="abs m-photo" role="img" aria-label="Photo of Bill Chao" style="background:linear-gradient(135deg,#f4c21c,#e9b98f)"></div>
  <h3 class="abs m-name">Bill Chao</h3><span class="abs m-tag">Mechanical Engineer</span>
  <p class="abs m-desc">We believe Steve can be a good fit as well for mentorship you are looking for!</p>
  <p class="abs m-price">$350/Month</p>
</article>
<article class="abs mentor" style="left:437px">
  <div class="abs m-photo" role="img" aria-label="Photo of Mike Satellite" style="background:linear-gradient(135deg,#1f2a36,#3b5b78)"></div>
  <h3 class="abs m-name">Mike Satellite</h3><span class="abs m-tag">Motivational Speaker</span>
  <p class="abs m-desc">We believe Steve can be a good fit as well for mentorship you are looking for!</p>
  <p class="abs m-price">$350/Month</p>
</article>

</body>
</html>
```